Business Card Design

I am a new realtor. To stand out from the other 25 realtors in my firm I need a card that will stand out. I am the youngest realtor here, so I want something to reflect that. Something different, as opposed to the same old traditional, boring cards everyone else has. It of course needs to have my picture which I will download for you ( I included a black and white option as well as color. Either are fine) and you can crop it or do whatever you need to make it look the best. Our company colors are red and white. These don't have to be the only colors on the card, but the red especially needs to be a focal color. I like a clean, stream-line look while still eye-catching. Not over the top busy.
While I do have to provide the company logo, I am a contractor. Therefore, I want the focus on me and my information.
Industry/Entity Type
Realtor
Contact Information for Business Card
Marissa Dunholt
Realtor (this needs the realtor logo which has the R in the circle at the end)
(office)555.318.4620
(cell) 555.742.9037
Mdunholt@brv-homesale.example
It will also need our company logo which I will download and send
Requirements
Nice to have
- I like the look of the foil or metallic. However, this is definitely not a requirement

```html
<!DOCTYPE html>
<html lang="en">
<head>
<meta charset="utf-8">
<title>Realtor Business Card</title>
<link rel="stylesheet" href="https://fonts.googleapis.com/css2?family=Tinos&family=Parisienne&family=Roboto:wght@400&display=swap">
<style>
  :root {
    --brand-red: #d71920;
    --band-red: #e03a3c;
    --paper: #ffffff;
    --ink: #1d1d1d;
    --backdrop: #e6e7ea;
    --photo-top: #c99f86;
    --photo-bottom: #7a4a32;
  }
  * { margin: 0; padding: 0; box-sizing: border-box; }
  html, body { width: 1200px; height: 800px; overflow: hidden; }
  body { background: var(--backdrop); position: relative; font-family: "Roboto", Arial, sans-serif; }

  .card { position: absolute; box-shadow: 0 4px 14px rgba(0,0,0,0.12); overflow: hidden; }

  /* Company side */
  .card--company {
    left: 90px; top: 252px; width: 530px; height: 303px;
    background: var(--brand-red);
    display: flex; align-items: center; justify-content: center;
  }
  .company-name {
    color: var(--paper);
    font-family: "Tinos", "Times New Roman", serif;
    font-size: 34px; letter-spacing: 1px; text-align: center; line-height: 1.2;
    text-transform: uppercase;
  }

  /* Agent side */
  .card--agent {
    left: 770px; top: 118px; width: 320px; height: 564px;
    background: var(--paper);
  }
  .portrait {
    position: absolute; left: 55px; top: 58px; width: 210px; height: 210px;
    border-radius: 50%; border: 5px solid var(--brand-red);
    background: linear-gradient(160deg, var(--photo-top), var(--photo-bottom));
  }
  .agent-name {
    position: absolute; left: 0; right: 0; top: 292px; text-align: center;
    font-family: "Parisienne", cursive; font-size: 36px; color: var(--ink);
  }
  .agent-name .initial { color: var(--brand-red); }
  .agent-title {
    position: absolute; left: 0; right: 0; top: 340px; text-align: center;
    font-size: 16px; color: var(--ink);
  }
  .contact-band { position: absolute; left: 0; top: 380px; width: 320px; height: 184px; }
  .contact-list {
    position: absolute; left: 0; right: 0; top: 448px; list-style: none;
    color: var(--paper); font-size: 13px; text-align: center; line-height: 2;
  }
  .contact-list li { display: flex; align-items: center; justify-content: center; gap: 6px; }
  .contact-list .sep { width: 10px; }
  .icon { width: 11px; height: 11px; fill: var(--paper); }
</style>
</head>
<body>

  <section class="card card--company" aria-label="Company side">
    <p class="company-name">Harriet Vale<br>&amp; Company</p>
  </section>

  <section class="card card--agent" aria-label="Agent side">
    <div class="portrait" role="img" aria-label="Portrait photo of the realtor"></div>
    <h1 class="agent-name"><span class="initial">M</span>arissa <span class="initial">D</span>unholt</h1>
    <p class="agent-title">Realtor ®</p>

    <svg class="contact-band" viewBox="0 0 320 184" aria-hidden="true">
      <polygon points="0,24 196,24 206,12 216,24 216,0 320,0 320,184 0,184" fill="var(--band-red)"/>
    </svg>

    <ul class="contact-list">
      <li>
        <svg class="icon" viewBox="0 0 12 12"><path d="M1 4 Q6 0 11 4 L9 5.5 L8 4.5 Q6 3.8 4 4.5 L3 5.5 Z M3 6 H9 L10 11 H2 Z"/></svg>
        555.318.4620
        <span class="sep"></span>
        <svg class="icon" viewBox="0 0 12 12"><path d="M3 0 H9 V12 H3 Z M4 1.5 V9 H8 V1.5 Z"/></svg>
        555.742.9037
      </li>
      <li>
        <svg class="icon" viewBox="0 0 12 12"><path d="M0 2 H12 V10 H0 Z M1 3 L6 7 L11 3 Z" fill-rule="evenodd"/></svg>
        Mdunholt@brv-homesale.example
      </li>
    </ul>
  </section>

</body>
</html>
```